PPT template for boutique strategic planning, accounting and taxation firm

We are a boutique firm that provides strategic, accounting and tax advice to our clients. The work we are doing is increasingly strategic work and we are required to produce reports and presentations and our current templates are simply not sufficient.
As you can see from the examples attached, we have very limited skills in house re design! We have attached a PPT document and word document (that should be PPT) that we use regularly as examples of the content. Excel worksheets are regularly embedded into the presentation (in both blue and orange - see below re colours)
Not specific to one area but typically these clients are famous for their own brand and are creating value in their industry through creating their own brand and we want to produce documents of a similar standard.
A Powerpoint Document Slide Template
Cover page layout, back page, intermediate page heading, in colours and styles based on the logo, title styles, and an intermediate or chapter heading slide style. Many of our presentations contain slides with tables, diagrams, flowcharts and text, including simple lists of bullet points. As above, you will see in our style guide that we have three coloured logos – we would like one version in blue and one version in orange please. Again, the cover should be bold and draw attention but remain professional.
We are looking for something that works in both 4:3 and 16:9 (or two templates please)
We like a clear professional and simple look.
Deliverable: PowerPoint template file (.potx extension) for PowerPoint 2007 with at least a “cover” layout, a “title and content” layout, and a simplified slide layout, as well as “back cover”. Please embed any fonts used.
Target Market(s)
Many of our clients are retail clients or have strong brands of their own.
Industry/Entity Type
Accounting
Requirements
Must have
- Harrowby & Co logo on each page.
Must have a cover page (please be bold but professional)
A selection of "standard" slides - dot points, detailed written content, example diagrams, flow charts etc.
A back cover
Nice to have
- We would like to have a copy done in both the blue and orange versions attached. Happy for the winner to complete the other colour after the winner is selected.
Prefer Arial logo but open to suggestions. Must be easy to read and professional
Should not have
- Nothing cartoonish

```html
<!DOCTYPE html>
<html lang="en">
<head>
<meta charset="utf-8">
<title>Harrowby &amp; Co — Presentation Template</title>
<link href="https://fonts.googleapis.com/css2?family=Graduate&family=Cinzel:wght@400;700&family=Open+Sans:wght@400;700&display=swap" rel="stylesheet">
<style>
:root{
  --orange:#f7941d;
  --orange-deep:#ef7d1a;
  --ink:#3b3b3b;
  --paper:#f2f0ea;
  --canvas:#ffffff;
  --text:#4a4a4a;
}
*{box-sizing:border-box;margin:0;padding:0}
html,body{width:1200px;height:900px;overflow:hidden;background:var(--canvas)}
.canvas{position:relative;width:1200px;height:900px}
.slide{position:absolute;background:var(--paper);box-shadow:2px 4px 6px rgba(0,0,0,.35);overflow:hidden}
.corner{position:absolute;top:0;right:0;background:var(--orange);clip-path:polygon(0 0,100% 0,100% 100%);color:#fff;font:700 9px 'Open Sans',sans-serif;text-align:right;padding:6px 7px 0 0}
.corner--large{width:50px;height:42px}
.corner--small{width:34px;height:30px;padding:5px 5px 0 0;font-size:8px}
.corner--foot{top:auto;bottom:0;clip-path:polygon(100% 0,100% 100%,0 100%);display:flex;align-items:flex-end;justify-content:flex-end;padding:0 6px 4px 0}
.slide-title{position:absolute;font-family:'Graduate',serif;color:var(--orange);line-height:1}
.rule{position:absolute;height:2px;background:var(--ink)}
.ring{position:absolute;width:11px;height:11px;border:2px solid var(--orange);border-radius:50%;background:var(--paper)}
.ring::after{content:"";position:absolute;left:2px;top:2px;width:3px;height:3px;border-radius:50%;background:var(--orange)}
.content-title{position:absolute;font-family:'Cinzel',serif;color:#222;font-size:11px;font-weight:400}
.body-copy{position:absolute;font-family:'Cinzel',serif;color:var(--text);font-size:4.6px;line-height:6px}
.body-copy p{margin-bottom:3px}
.body-copy--small{font-size:3.6px;line-height:4.6px}
.body-copy--small p{margin-bottom:2px}
.chevron{position:absolute;width:12px;height:10px;background:var(--orange);clip-path:polygon(0 0,55% 0,100% 50%,55% 100%,0 100%,45% 50%)}
.divider{position:absolute;width:2px;background:var(--orange)}
.brand-foot{position:absolute;display:flex;align-items:center;gap:2px;font:700 6px 'Open Sans',sans-serif;color:var(--ink)}
.brand-foot i{display:block;width:7px;height:7px;border-radius:50%;background:var(--orange)}
.cover-title{position:absolute;left:0;right:0;top:20px;text-align:center;font-family:'Graduate',serif;font-size:44px;color:var(--orange-deep);line-height:1;letter-spacing:1px}
.cover-title--reflect{top:74px;transform:scaleY(-1);opacity:.12;-webkit-mask-image:linear-gradient(to top,#000,transparent 70%);mask-image:linear-gradient(to top,#000,transparent 70%)}
.cover-details{position:absolute;left:0;right:0;top:62px;text-align:center;font:700 9px 'Open Sans',sans-serif;color:#111;letter-spacing:.2px}
.cover-brand{position:absolute;left:0;right:0;top:154px;display:flex;justify-content:center;align-items:center;gap:6px;font:700 18px 'Open Sans',sans-serif;color:var(--orange)}
.cover-brand i{display:block;width:18px;height:18px;border-radius:50%;background:var(--orange)}
.cover-url{position:absolute;left:0;right:0;top:222px;text-align:center;font:400 9px 'Open Sans',sans-serif;color:#222}
.data-table{position:absolute;border:3px solid var(--orange);border-collapse:collapse}
.data-table td{border:2px solid var(--orange);width:56px;height:16px}
.bullets{position:absolute;font:700 5px 'Open Sans',sans-serif;color:var(--orange)}
.bullets .main{display:flex;align-items:center;gap:3px;margin-bottom:3px}
.bullets .subs{display:grid;grid-template-columns:auto auto;column-gap:8px;row-gap:3px;padding-left:4px}
.bullets .sub{display:flex;align-items:center;gap:2px;font:400 4px 'Cinzel',serif;color:#333}
.dot{display:block;width:5px;height:5px;border:1px solid var(--orange);border-radius:50%}
.col-head{position:absolute;font-family:'Cinzel',serif;font-size:11px;font-weight:400;color:#222}
.image-slot{position:absolute;background:linear-gradient(160deg,#f9a23a,var(--orange-deep))}
.badge{position:absolute;width:80px;height:80px;border-radius:50%;background:#231f20;color:#fff;font:400 8px 'Cinzel',serif;display:flex;align-items:center;justify-content:center}
.thanks{position:absolute;left:0;right:0;top:78px;text-align:center;font-family:'Graduate',serif;font-size:32px;color:var(--orange-deep);line-height:1}
.thanks--reflect{top:110px;transform:scaleY(-1);opacity:.35;color:#8fb3d9;-webkit-mask-image:linear-gradient(to top,#000,transparent 75%);mask-image:linear-gradient(to top,#000,transparent 75%)}
</style>
</head>
<body>
<main class="canvas">

  <!-- Cover -->
  <section class="slide" style="left:175px;top:35px;width:435px;height:245px">
    <h1 class="cover-title">TITLE PAGE</h1>
    <div class="cover-title cover-title--reflect" aria-hidden="true">TITLE PAGE</div>
    <p class="cover-details">DETAILS OF PRESENTATION / NAME OF PRESENTOR</p>
    <div class="cover-brand"><i></i>Harrowby &amp; Co</div>
    <p class="cover-url">http://www.harrowbyco-site.com/</p>
    <div class="corner corner--large corner--foot">01</div>
  </section>

  <!-- Two-column content -->
  <section class="slide" style="left:175px;top:302px;width:437px;height:246px">
    <h2 class="slide-title" style="left:22px;top:14px;font-size:24px">SLIDE TITLE</h2>
    <div class="rule" style="left:12px;top:43px;width:366px"></div>
    <div class="ring" style="left:5px;top:37px"></div>
    <div class="corner corner--large">04</div>
    <h3 class="content-title" style="left:16px;top:61px">Content Title</h3>
    <div class="chevron" style="left:16px;top:80px"></div>
    <div class="body-copy" style="left:42px;top:78px;width:155px">
      <p>Key findings on growth, margin and tax position are set out here for review by the board and partners. Key findings on growth, margin and tax position are set out here for review by the board and partners.</p>
      <p>Key findings on growth, margin and tax position are set out here for review by the board and partners. Key findings on growth, margin and tax position are set out here for review by the board and partners.</p>
      <p>Key findings on growth, margin and tax position are set out here for review by the board and partners. Key findings on growth, margin and tax position are set out here for review by the board and partners.</p>
      <p>Key findings on growth, margin and tax position are set out here for review by the board and partners. Key findings on growth, margin and tax position are set out here for review by the board and partners.</p>
    </div>
    <div class="divider" style="left:207px;top:70px;height:152px"></div>
    <div class="chevron" style="left:224px;top:80px"></div>
    <div class="body-copy" style="left:244px;top:78px;width:160px">
      <p>Key findings on growth, margin and tax position are set out here for review by the board and partners. Key findings on growth, margin and tax position are set out here for review by the board and partners.</p>
      <p>Key findings on growth, margin and tax position are set out here for review by the board and partners. Key findings on growth, margin and tax position are set out here for review by the board and partners.</p>
    </div>
    <div class="chevron" style="left:224px;top:157px"></div>
    <div class="body-copy" style="left:244px;top:155px;width:160px">
      <p>Key findings on growth, margin and tax position are set out here for review by the board and partners. Key findings on growth, margin and tax position are set out here for review by the board and partners.</p>
      <p>Key findings on growth, margin and tax position are set out here for review by the board and partners. Key findings on growth, margin and tax position are set out here for review by the board and partners.</p>
    </div>
    <div class="brand-foot" style="left:182px;top:233px"><i></i>Harrowby &amp; Co</div>
  </section>

  <!-- Content with image -->
  <section class="slide" style="left:175px;top:567px;width:438px;height:248px">
    <h2 class="slide-title" style="left:22px;top:14px;font-size:24px">SLIDE TITLE</h2>
    <div class="rule" style="left:12px;top:43px;width:366px"></div>
    <div class="ring" style="left:5px;top:37px"></div>
    <div class="corner corner--large">04</div>
    <h3 class="content-title" style="left:16px;top:61px">Content Title</h3>
    <div class="chevron" style="left:16px;top:80px"></div>
    <div class="body-copy" style="left:40px;top:78px;width:250px">
      <p>Key findings on growth, margin and tax position are set out here for review by the board and partners. Key findings on growth, margin and tax position are set out here for review by the board and partners.</p>
      <p>Key findings on growth, margin and tax position are set out here for review by the board and partners. Key findings on growth, margin and tax position are set out here for review by the board and partners.</p>
      <p>Key findings on growth, margin and tax position are set out here for review by the board and partners. Key findings on growth, margin and tax position are set out here for review by the board and partners.</p>
      <p>Key findings on growth, margin and tax position are set out here for review by the board and partners. Key findings on growth, margin and tax position are set out here for review by the board and partners.</p>
      <p>Key findings on growth, margin and tax position are set out here for review by the board and partners. Key findings on growth, margin and tax position are set out here for review by the board and partners.</p>
      <p>Key findings on growth, margin and tax position are set out here for review by the board and partners. Key findings on growth, margin and tax position are set out here for review by the board and partners.</p>
    </div>
    <div class="image-slot" role="img" aria-label="Image placeholder for a supporting photograph" style="left:300px;top:85px;width:108px;height:112px"></div>
    <div class="brand-foot" style="left:182px;top:234px"><i></i>Harrowby &amp; Co</div>
  </section>
  <div class="badge" style="left:527px;top:765px">WITH IMAGE</div>

  <!-- Graphic slide -->
  <section class="slide" style="left:638px;top:72px;width:320px;height:178px">
    <h2 class="slide-title" style="left:20px;top:9px;font-size:17px">GRAPHIC SLIDE</h2>
    <div class="rule" style="left:8px;top:30px;width:272px;height:1.5px"></div>
    <div class="corner corner--small">04</div>
    <svg style="position:absolute;left:14px;top:62px" width="145" height="90" viewBox="0 0 145 90">
      <polygon points="55,8 82,8 90,24 47,24" fill="#8cc63f"/>
      <polygon points="47,24 90,24 92,30 45,30" fill="#5e9e2a"/>
      <polygon points="37,34 100,34 116,55 21,55" fill="#f7941d"/>
      <polygon points="21,55 116,55 118,60 19,60" fill="#c76f12"/>
      <polygon points="14,64 124,64 140,82 0,82" fill="#4a4a4a"/>
      <polygon points="0,82 140,82 140,87 0,87" fill="#2e2e2e"/>
    </svg>
    <svg style="position:absolute;left:183px;top:50px" width="95" height="100" viewBox="0 0 95 100">
      <ellipse cx="45" cy="52" rx="44" ry="41" fill="#7a5a3a"/>
      <path d="M45 45 L45 4 A44 41 0 0 1 79 19 Z" fill="#2fb77a"/>
      <path d="M45 45 L79 19 A44 41 0 0 1 89 45 Z" fill="#1aa89a"/>
      <path d="M45 45 L89 45 A44 41 0 0 1 70 80 Z" fill="#f7941d"/>
      <path d="M45 45 L70 80 A44 41 0 0 1 22 82 Z" fill="#c49a6c"/>
      <path d="M45 45 L22 82 A44 41 0 0 1 1 45 Z" fill="#5e5e5e"/>
      <path d="M45 45 L1 45 A44 41 0 0 1 14 16 Z" fill="#8cc63f"/>
      <path d="M45 45 L14 16 A44 41 0 0 1 45 4 Z" fill="#1f9b48"/>
    </svg>
    <div class="brand-foot" style="left:142px;top:166px"><i></i>Harrowby &amp; Co</div>
  </section>

  <!-- Text slide -->
  <section class="slide" style="left:638px;top:265px;width:320px;height:180px">
    <h2 class="slide-title" style="left:20px;top:9px;font-size:17px">SLIDE TITLE</h2>
    <div class="rule" style="left:8px;top:30px;width:272px;height:1.5px"></div>
    <div class="corner corner--small">04</div>
    <h3 class="content-title" style="left:15px;top:43px;font-size:9px">Content Title</h3>
    <div class="chevron" style="left:15px;top:56px;width:9px;height:8px"></div>
    <div class="body-copy body-copy--small" style="left:30px;top:55px;width:170px">
      <p>Key findings on growth, margin and tax position are set out here for review by the board and partners. Key findings on growth, margin and tax position are set out here for review by the board and partners.</p>
      <p>Key findings on growth, margin and tax position are set out here for review by the board and partners. Key findings on growth, margin and tax position are set out here for review by the board and partners.</p>
      <p>Key findings on growth, margin and tax position are set out here for review by the board and partners. Key findings on growth, margin and tax position are set out here for review by the board and partners.</p>
      <p>Key findings on growth, margin and tax position are set out here for review by the board and partners. Key findings on growth, margin and tax position are set out here for review by the board and partners.</p>
      <p>Key findings on growth, margin and tax position are set out here for review by the board and partners. Key findings on growth, margin and tax position are set out here for review by the board and partners.</p>
      <p>Key findings on growth, margin and tax position are set out here for review by the board and partners. Key findings on growth, margin and tax position are set out here for review by the board and partners.</p>
    </div>
    <div class="brand-foot" style="left:142px;top:167px"><i></i>Harrowby &amp; Co</div>
  </section>

  <!-- Bullets and table -->
  <section class="slide" style="left:638px;top:465px;width:320px;height:178px">
    <h2 class="slide-title" style="left:20px;top:9px;font-size:17px">SLIDE TITLE</h2>
    <div class="rule" style="left:8px;top:30px;width:272px;height:1.5px"></div>
    <div class="corner corner--small">04</div>
    <h3 class="col-head" style="left:36px;top:42px">Bullet Form</h3>
    <h3 class="col-head" style="left:227px;top:42px">Table</h3>
    <div class="divider" style="left:160px;top:50px;height:112px"></div>
    <div class="bullets" style="left:29px;top:70px">
      <div class="main"><span class="dot"></span>MAIN BULLET</div>
      <div class="subs">
        <div class="sub"><span class="dot"></span>Subbullet form</div><div class="sub"><span class="dot"></span>Subbullet form</div>
        <div class="sub"><span class="dot"></span>Subbullet form</div><div class="sub"><span class="dot"></span>Subbullet form</div>
        <div class="sub"><span class="dot"></span>Subbullet form</div><div class="sub"><span class="dot"></span>Subbullet form</div>
        <div class="sub"><span class="dot"></span>Subbullet form</div><div class="sub"><span class="dot"></span>Subbullet form</div>
        <div class="sub"><span class="dot"></span>Subbullet form</div><div class="sub"><span class="dot"></span>Subbullet form</div>
        <div class="sub"><span class="dot"></span>Subbullet form</div><div class="sub"><span class="dot"></span>Subbullet form</div>
      </div>
    </div>
    <table class="data-table" style="left:188px;top:58px">
      <tr><td></td><td></td></tr><tr><td></td><td></td></tr><tr><td></td><td></td></tr>
      <tr><td></td><td></td></tr><tr><td></td><td></td></tr><tr><td></td><td></td></tr>
    </table>
  </section>

  <!-- Back cover -->
  <section class="slide" style="left:638px;top:650px;width:320px;height:180px">
    <h2 class="thanks">THANK YOU</h2>
    <div class="thanks thanks--reflect" aria-hidden="true">THANK YOU</div>
    <div class="brand-foot" style="left:142px;top:169px"><i></i>Harrowby &amp; Co</div>
    <div class="corner corner--small corner--foot">X</div>
  </section>

</main>
</body>
</html>
```